Need posters that inspire entrepreneurs

I want to create beautiful, inspiring wall art. I'm looking for a designer to create an awesome sample (note this sample is not for real use). The winning design will form the foundation of our art "style" so there will be LOTS of ongoing work for the winning designer.

It's your challenge to create a style that is clean, inspiring and timeless, and possibly can be adapted to different colour palettes.

Looking for a perfect execution of words, image and design.

The attached example shows one idea. It should serve as an idea only.

Format of the images should be either rectangular or square. Exact size is preferably UK A4 (US letter) or max A3. Assume that a display would consist of a 4 x 4 image grid so size needs to allow for that in a small to medium size office.

The quotes I want in the 3 samples (each in an individual poster - not combined in 1 poster). Each quote should have it's own, the reason for three is to prove the design work on more than one quote. The quotes are:

1) Failure is the condiment that gives success its flavor.
– Dorian Welsby

2) Whether you think you can or think you can’t, you’re right.
– Oswald Pike

3) Ever tried. Ever failed. No matter. Try Again. Fail again. Fail better.
– Lionel Marwick

Each design should include the image of the person and the quote + any design elements you consider relevant. You should find relevant images of the individuals being quoted. The final images will not be published or used commercially in any way.

Font styles to use
Serif
Sans Serif

Colors

Designer to choose colors to be used in the design.

Requirements
Must have
• Words and headshot image - 1 per poster design.
• Please consider in the design that there will not always be photographs of the person quoted and as such the design will need to hold, whether the source is a photo, sketch or something else.
Nice to have
• None, but note that the final image will be printed on a wall mounted board, printed to the edge but not on the edge. The board will have black or white edges so consider in the design.
Should not have
• None

```html
<!DOCTYPE html>
<html lang="en">
<head>
<meta charset="utf-8">
<title>Fail Better — Lionel Marwick</title>
<link href="https://fonts.googleapis.com/css2?family=Cormorant+Garamond:wght@400;500;700&display=swap" rel="stylesheet">
<style>
  :root {
    --poster-bg: #000000;
    --ink: #f2f2f2;
    --ink-soft: #bdbdbd;
    --ghost: #161616;
    --rule: #6e6e6e;
    --photo-light: #8a8a8a;
    --photo-mid: #3a3a3a;
  }
  html, body {
    margin: 0;
    padding: 0;
    width: 1200px;
    height: 848px;
    overflow: hidden;
    background: var(--poster-bg);
  }
  .poster {
    position: relative;
    width: 1200px;
    height: 848px;
    background: var(--poster-bg);
    overflow: hidden;
    font-family: "Cormorant Garamond", Georgia, serif;
    color: var(--ink);
  }
  .portrait {
    position: absolute;
    left: 470px;
    top: 0;
    width: 730px;
    height: 848px;
    background:
      radial-gradient(ellipse 260px 330px at 470px 330px, var(--photo-light) 0%, var(--photo-mid) 45%, transparent 80%),
      radial-gradient(ellipse 300px 260px at 480px 760px, #2a2a2a 0%, transparent 75%),
      linear-gradient(90deg, var(--poster-bg) 0%, #0b0b0b 40%, #111 100%);
  }
  .ghost-words {
    position: absolute;
    font-weight: 700;
    color: var(--ghost);
    white-space: nowrap;
    line-height: 0.82;
    transform-origin: left top;
    letter-spacing: 1px;
  }
  .ghost-left {
    left: 24px;
    top: 848px;
    font-size: 92px;
    transform: rotate(-90deg);
  }
  .ghost-right {
    left: 1104px;
    top: 0;
    font-size: 70px;
    transform: rotate(90deg) translate(40px, -64px);
    color: #1c1c1c;
  }
  .quote {
    position: absolute;
    left: 0;
    width: 740px;
    text-align: center;
    font-size: 40px;
    font-weight: 400;
    letter-spacing: 6px;
    line-height: 42px;
    margin: 0;
  }
  .quote strong { font-weight: 700; }
  .quote-first { top: 227px; }
  .quote-second { top: 442px; }
  .quote span { display: block; }
  .attribution {
    position: absolute;
    left: 265px;
    top: 640px;
    width: 232px;
    text-align: center;
  }
  .signature {
    width: 120px;
    height: 30px;
    margin: 0 auto 10px;
    background: linear-gradient(90deg, transparent, #2b2b2b 20%, #2b2b2b 80%, transparent);
    border-radius: 15px;
  }
  .attribution-rule {
    height: 1px;
    background: var(--rule);
    margin-bottom: 8px;
  }
  .attribution-name {
    font-size: 15px;
    letter-spacing: 1.5px;
    color: var(--ink-soft);
    margin: 0;
  }
  .attribution-dates {
    font-size: 12px;
    color: var(--ink-soft);
    margin: 2px 0 0;
  }
</style>
</head>
<body>
  <main class="poster">
    <div class="portrait" role="img" aria-label="Black and white portrait of Lionel Marwick in a dark suit and tie, glasses pushed up on his forehead"></div>

    <div class="ghost-words ghost-left" aria-hidden="true">EVER TRIED.<br>EVER FAILED.<br>NO MATTER.</div>
    <div class="ghost-words ghost-right" aria-hidden="true">FAIL BETTER.</div>

    <p class="quote quote-first">
      <span>EVER <strong>TRIED</strong>.</span>
      <span><strong>EVER</strong> FAILED.</span>
      <span>NO MATTER.</span>
    </p>
    <p class="quote quote-second">
      <span><strong>TRY</strong> AGAIN.</span>
      <span>FAIL <strong>AGAIN</strong>.</span>
      <span>FAIL <strong>BETTER</strong>.</span>
    </p>

    <div class="attribution">
      <div class="signature" role="img" aria-label="Handwritten signature of Lionel Marwick"></div>
      <div class="attribution-rule"></div>
      <p class="attribution-name">LIONEL MARWICK</p>
      <p class="attribution-dates">(1906-1989)</p>
    </div>
  </main>
</body>
</html>
```